Modern, Playful Illustrated Book Cover for Women’s Wellness / Self-Help Book

Project Scope
This contest is for the front cover only of a 6x9 nonfiction book. This contest is for the front cover only. The spine and back cover will be completed at a later stage once final production specifications are available.

Title:
Lemons! She’s Set to Juggle Them

Subtitle:
40 Morning Prompts and Gentle Routines to Steady Moods, Grow Calm Rituals, and Renew Your Days

Author:
Delphine Okoro, M.Ed.

I want a modern, playful, bold, polished illustrated cover that feels like a contemporary women’s wellness/self-help book — not a traditional diet book.

The cover should especially resonate with Black women, while still feeling welcoming to a broader female audience.

Illustration only — no photography and no real people.

If hands or other human elements are included, they should be fully illustrated as Black women using rich brown skin tones in a modern, sophisticated way.

Please do not use black silhouettes, shadow figures, faceless silhouette-style people, or generic darkened human shapes. I want the representation to feel intentional, contemporary, and fully illustrated.

I am open to creative interpretations around themes such as:

everyday choices
habits
cravings and temptation
changing patterns
letting go
taking back control
progress
reclaiming your life

The title should be the visual star and should remain easy to read at thumbnail size.

Please avoid:

bathroom scales as the main image
measuring tape
before-and-after bodies
body silhouettes
generic fitness imagery
salads or smoothies as the main concept
medical or clinical imagery
childish cartoons
generic stock-vector or template-looking designs

I want the overall feel to be fresh, modern, warm, confident, playful, sophisticated, and visually engaging.

Originality
Please create an original concept specifically for this book. Do not recreate or closely imitate an existing published book cover.

Target Market(s)

Adult women, especially Black women, who want a practical, encouraging, realistic approach to weight loss, healthier habits, and sustainable change. Must haves

Industry/Entity Type

Publishing / Books / Wellness / Self-Help

Requirements
Must have
• Modern illustrated cover; strong, highly readable title; polished contemporary wellness/self-help feel; illustration only, no photography; if human elements are used, they should reflect Black women with rich brown skin tones; front cover only.
Nice to have
• Creative visual ideas around everyday choices, habits, cravings, letting go, progress, and taking back control. Open to illustrated hands, food-related interactions, everyday objects, or symbolic imagery if used in a sophisticated way. Colors: Open to designer color recommendations; I prefer a fresh, modern, warm, energetic, sophisticated palette.
Should not have
• No black silhouettes or shadow figures; no real people or photography; no scales as the main image; no measuring tape, before/after bodies, body silhouettes, generic fitness imagery, salads/smoothies as the main concept, medical imagery, childish cartoons, or generic template/stock-vector-looking designs.

```html
<!DOCTYPE html>
<html lang="en">
<head>
<meta charset="utf-8">
<title>Lemons! She’s Set to Juggle Them — Front Cover</title>
<link rel="stylesheet" href="https://fonts.googleapis.com/css2?family=Abril+Fatface&family=Jost:wght@400;500&family=Lexend:wght@300;400&display=swap">
<style>
  :root {
    --stage: #e8e2dc;
    --paper: #f6f4f3;
    --plum: #4e0a2e;
    --coral: #f0645c;
    --blush: #e5a5b8;
    --cocoa: #3b2a14;
    --rule: #d9a9b8;
    --wine-text: #6b1238;
  }
  * { margin: 0; padding: 0; box-sizing: border-box; }
  html, body {
    width: 1200px;
    height: 806px;
    overflow: hidden;
    background: var(--stage);
  }
  .stage {
    width: 1200px;
    height: 806px;
    display: flex;
    align-items: center;
    justify-content: center;
  }
  .cover {
    position: relative;
    width: 493px;
    height: 740px;
    background: var(--paper);
    box-shadow: 0 10px 30px rgba(60, 40, 30, 0.18);
    overflow: hidden;
  }
  .cover-art {
    position: absolute;
    inset: 0;
    width: 100%;
    height: 100%;
  }
  .subtitle {
    position: absolute;
    top: 62px;
    left: 0;
    right: 0;
    text-align: center;
    font-family: "Lexend", sans-serif;
    font-weight: 300;
    font-size: 15px;
    line-height: 20.5px;
    color: var(--wine-text);
    letter-spacing: -0.2px;
  }
  .subtitle .lead { font-weight: 400; }
  .title {
    position: absolute;
    left: 0;
    right: 0;
    text-align: center;
  }
  .title-top {
    top: 206px;
    font-family: "Abril Fatface", serif;
    font-size: 84px;
    line-height: 1;
    color: var(--plum);
    letter-spacing: -2px;
  }
  .title-top .bang { color: var(--blush); }
  .title-mid {
    top: 330px;
    display: flex;
    align-items: center;
    justify-content: center;
    gap: 12px;
    font-family: "Jost", sans-serif;
    font-weight: 400;
    font-size: 31px;
    line-height: 1;
    color: var(--cocoa);
    letter-spacing: -0.5px;
  }
  .title-mid .rule {
    width: 72px;
    height: 1px;
    background: var(--rule);
  }
  .title-bottom {
    top: 392px;
    font-family: "Abril Fatface", serif;
    font-size: 62px;
    line-height: 1;
    color: var(--coral);
    letter-spacing: -1.5px;
  }
  .flourish {
    position: absolute;
  }
  .flourish-top { left: 70px; top: 158px; width: 62px; height: 46px; }
  .flourish-bottom { left: 372px; top: 444px; width: 80px; height: 60px; }
  .author {
    position: absolute;
    top: 642px;
    left: 0;
    right: 0;
    text-align: center;
    font-family: "Jost", sans-serif;
    font-weight: 500;
    font-size: 23px;
    color: var(--cocoa);
    letter-spacing: -0.3px;
  }
</style>
</head>
<body>
<main class="stage">
  <article class="cover">
    <svg class="cover-art" viewBox="0 0 493 740" role="img" aria-label="Soft blurred abstract wave of warm rust and blush tones sweeping across the lower cover">
      <defs>
        <radialGradient id="wave-warm" cx="0.35" cy="0.5" r="0.6">
          <stop offset="0" stop-color="#b4523a" stop-opacity="0.55"/>
          <stop offset="0.45" stop-color="#e7a98f" stop-opacity="0.35"/>
          <stop offset="1" stop-color="#f6f4f3" stop-opacity="0"/>
        </radialGradient>
        <radialGradient id="wave-blush" cx="0.5" cy="0.5" r="0.5">
          <stop offset="0" stop-color="#f2c3b2" stop-opacity="0.5"/>
          <stop offset="1" stop-color="#f6f4f3" stop-opacity="0"/>
        </radialGradient>
        <linearGradient id="base-fade" x1="0" y1="0" x2="0" y2="1">
          <stop offset="0.6" stop-color="#f6f4f3" stop-opacity="0"/>
          <stop offset="1" stop-color="#dcd6d4" stop-opacity="0.8"/>
        </linearGradient>
      </defs>
      <ellipse cx="150" cy="570" rx="240" ry="110" fill="url(#wave-warm)"/>
      <ellipse cx="420" cy="600" rx="160" ry="90" fill="url(#wave-blush)"/>
      <rect width="493" height="740" fill="url(#base-fade)"/>
    </svg>

    <p class="subtitle">
      <span class="lead">40 Morning Prompts &amp; Gentle Routines</span><br>
      to Steady Moods, Grow Calm Rituals,<br>
      and Renew Your Days
    </p>

    <svg class="flourish flourish-top" viewBox="0 0 62 46" role="img" aria-label="Small coral calligraphic flourish">
      <ellipse cx="31" cy="23" rx="28" ry="16" fill="#f4b6ad" opacity="0.35"/>
    </svg>

    <h1 class="title title-top">Lemons<span class="bang">!</span></h1>
    <p class="title title-mid"><span class="rule"></span>SHE’S SET TO<span class="rule"></span></p>
    <p class="title title-bottom">Juggle Them.</p>

    <svg class="flourish flourish-bottom" viewBox="0 0 80 60" role="img" aria-label="Small pink decorative swirl ornament">
      <ellipse cx="42" cy="28" rx="34" ry="22" fill="#e5a5b8" opacity="0.3"/>
    </svg>

    <p class="author">DELPHINE OKORO | M.ED</p>
  </article>
</main>
</body>
</html>
```